Corvel Tide Supply Business Cards

I need a business card design for my business. We specialise in supplying quality brand cleaning products for boats
Updates

Target Market(s)

local household people with personal boats

Industry/Entity Type

Business

Requirements
Must have
• Address - 14 Fenwick Turn, Marlow WA 6802
Phone - 0461 382 917
Email - corveltidesupply@quillnet.com
Web - www.corveltidesupply.com.au
Warren Hale
Director

Business logo is a must have
Nice to have
• Glennox logo is optional but recommended as it shows what we do

```html
<!DOCTYPE html>
<html lang="en">
<head>
<meta charset="utf-8">
<title>Corvel Tide Supply – Business Cards</title>
<link href="https://fonts.googleapis.com/css2?family=Arimo:wght@400;700&display=swap" rel="stylesheet">
<style>
  :root {
    --backdrop: #474747;
    --card-white: #ffffff;
    --marine-blue: #0c4a84;
    --sea-light: #2f6fae;
    --mark-tint: #dbe6f1;
    --accent-orange: #e8761c;
    --text-white: #ffffff;
  }
  * { margin: 0; padding: 0; box-sizing: border-box; }
  html, body {
    width: 1200px; height: 426px; overflow: hidden;
    background: var(--backdrop);
    font-family: "Arimo", Arial, sans-serif;
  }
  .sheet { position: relative; width: 1200px; height: 426px; }
  .card {
    position: absolute; top: 56px;
    width: 536px; height: 314px;
    border-radius: 20px; overflow: hidden;
    background: var(--card-white);
  }
  .card--front { left: 60px; }
  .card--back { left: 616px; }
  .card__waves { position: absolute; inset: 0; width: 100%; height: 100%; }

  .brand-mark {
    position: absolute; border-radius: 50%;
    background: var(--mark-tint);
  }
  .card--front .brand-mark { left: 218px; top: 22px; width: 100px; height: 100px; }
  .card--back .brand-mark { left: 72px; top: 26px; width: 40px; height: 40px; }

  .brand-name {
    position: absolute; left: 0; right: 0;
    text-align: center; color: var(--text-white);
    font-weight: 400; text-transform: uppercase;
  }
  .card--front .brand-name--main { top: 190px; font-size: 38px; letter-spacing: 6px; line-height: 46px; }
  .brand-divider {
    position: absolute; left: 136px; right: 136px; top: 240px;
    height: 1px; background: var(--text-white);
  }
  .card--front .brand-name--sub { top: 246px; font-size: 19px; letter-spacing: 5px; line-height: 24px; }

  .brand-small {
    position: absolute; left: 22px; width: 140px; top: 72px;
    text-align: center; color: var(--marine-blue);
    font-size: 11px; letter-spacing: 2px; line-height: 14px;
    text-transform: uppercase;
  }
  .contact-person {
    position: absolute; left: 314px; width: 140px; top: 60px;
    text-align: center; font-size: 15px; line-height: 21px;
  }
  .contact-person__name { color: var(--marine-blue); }
  .contact-person__role { color: var(--accent-orange); font-weight: 700; }

  .contact-address {
    position: absolute; left: 0; right: 0; top: 192px;
    text-align: center; color: var(--text-white); font-size: 13px;
  }
  .contact-list {
    position: absolute; left: 136px; top: 216px;
    list-style: none; color: var(--text-white); font-size: 13px;
  }
  .contact-list li { display: flex; align-items: center; height: 26px; }
  .contact-list svg { width: 16px; height: 16px; margin-right: 14px; flex: none; }
</style>
</head>
<body>
<main class="sheet">

  <section class="card card--front" aria-label="Card front">
    <svg class="card__waves" viewBox="0 0 536 314" preserveAspectRatio="none" aria-hidden="true">
      <path d="M0 150 C90 130 170 150 260 164 C360 178 450 150 536 126 L536 314 L0 314 Z" fill="var(--marine-blue)"/>
      <path d="M0 138 C120 110 220 160 320 152 C400 146 470 130 536 118 L536 124 C470 138 400 156 320 160 C220 166 120 124 0 146 Z" fill="var(--marine-blue)"/>
    </svg>
    <div class="brand-mark" aria-hidden="true"></div>
    <p class="brand-name brand-name--main">Corvel Tide</p>
    <div class="brand-divider"></div>
    <p class="brand-name brand-name--sub">Supply</p>
  </section>

  <section class="card card--back" aria-label="Card back">
    <svg class="card__waves" viewBox="0 0 536 314" preserveAspectRatio="none" aria-hidden="true">
      <path d="M0 150 C120 138 220 158 320 146 C410 136 470 140 536 146" fill="none" stroke="var(--marine-blue)" stroke-width="3"/>
      <path d="M0 176 C110 162 200 180 300 172 C400 164 470 162 536 170 L536 314 L0 314 Z" fill="var(--marine-blue)"/>
      <path d="M0 184 C120 170 210 190 310 180 C400 172 470 172 536 178" fill="none" stroke="var(--sea-light)" stroke-width="2"/>
    </svg>
    <div class="brand-mark" aria-hidden="true"></div>
    <p class="brand-small">Corvel Tide Supply</p>
    <div class="contact-person">
      <p class="contact-person__name">Warren Hale</p>
      <p class="contact-person__role">Director</p>
    </div>
    <p class="contact-address">14 Fenwick Turn, Marlow WA 6802</p>
    <ul class="contact-list">
      <li>
        <svg viewBox="0 0 16 16" aria-hidden="true"><rect x="1" y="1" width="14" height="14" rx="2" fill="var(--text-white)"/><path d="M5 4 L7 4 L7.5 6.5 L6.5 7.5 C7 8.6 7.6 9.2 8.5 9.6 L9.5 8.6 L12 9 L12 11 C8 11.5 4.5 8 5 4 Z" fill="var(--marine-blue)"/></svg>
        0461 382 917
      </li>
      <li>
        <svg viewBox="0 0 16 16" aria-hidden="true"><rect x="1" y="3" width="14" height="10" rx="1" fill="var(--text-white)"/><path d="M1.5 3.5 L8 9 L14.5 3.5" fill="none" stroke="var(--marine-blue)" stroke-width="1.2"/></svg>
        corveltidesupply@quillnet.com
      </li>
      <li>
        <svg viewBox="0 0 16 16" aria-hidden="true"><circle cx="8" cy="8" r="7" fill="var(--text-white)"/><ellipse cx="8" cy="8" rx="3" ry="7" fill="none" stroke="var(--marine-blue)" stroke-width="1"/><path d="M1 8 H15" stroke="var(--marine-blue)" stroke-width="1"/></svg>
        www.corveltidesupply.com.au
      </li>
    </ul>
  </section>

</main>
</body>
</html>
```